New packaging company website**

We are looking for a new design for our corporate website (www.borvellotrade.it). The theme must be made with Elementor and Crocoblock plugins. Currently the demo site can be reached at www.borvellotrade.cloud

You can also check our current site for your reference www.borvellotrade.it
We mainly deal with the resale of industrial containers for companies, most of our customers are B2B but also a good number of private customers. The site must therefore be accessible to all and the prices always visible even without registration or other.

Given the heterogeneity of our articles, we need a very clear shop page, with clearly visible filters and possibly with a list view and a table.

However, it does not have to be a simple ecommerce, we still want a site with many texts, spaces for product FAQs, tooltips on filters or attributes.

Target Market(s)

90% B2B

Coding

Coded - Design and coding required

Requirements
Must have
• beautiful, modern and captivating graphics. It must be a "full" site and not a flat one.
Nice to have
• We are undecided about the location of the main product menu.

If you leave the top bar with the icons and labels of the macro categories, as happens now on the live site and on the demo site.

Or if you want to insert the classic "all categories" on the top menu (https://fernalux.qorvidex.com/demo-tools/demo/tools/ or https://www.velmiratheme.com/wordpress/velmira/shop30/)

Or if you want to take advantage of something more modern, such as the sidebar menu (https://www.velmiratheme.com/wordpress/velmira/shop10/ or https://www.velmiratheme.com/wordpress/velmira/shop19/)

```html
<!DOCTYPE html>
<html lang="en">
<head>
<meta charset="utf-8">
<title>Borvello Trade – Industrial Containers</title>
<link href="https://fonts.googleapis.com/css2?family=Oswald:wght@500;600&family=Roboto:wght@400;500;700&display=swap" rel="stylesheet">
<style>
:root{
  --navy:#13457c;
  --blue:#2b8bcc;
  --ink:#222;
  --muted:#444;
  --mist:#e1e9f1;
  --white:#fff;
}
*{box-sizing:border-box;margin:0;padding:0}
html,body{width:1200px;height:4257px;overflow:hidden}
body{position:relative;font-family:"Roboto",sans-serif;color:var(--ink);background:var(--white);font-size:13px}
.abs{position:absolute}
.head{font-family:"Oswald",sans-serif;font-weight:600;text-transform:uppercase;letter-spacing:.2px}
.section{position:absolute;left:0;width:1200px}
/* top bar */
.topbar{top:0;height:50px;border-bottom:1px solid #ddd;font-size:10px;font-weight:700;text-transform:uppercase}
.topbar .links{left:111px;top:19px;word-spacing:6px}
.topbar .right{left:835px;top:19px;word-spacing:6px}
.social{left:515px;top:13px;display:flex;gap:11px}
.social span{width:22px;height:22px;border:1.5px solid #333;border-radius:50%}
/* header */
.brand{left:115px;top:78px;display:flex;align-items:center;gap:10px;color:var(--navy);font-family:"Oswald",sans-serif;font-weight:600;font-size:30px}
.brand i{width:36px;height:36px;background:var(--navy);border-radius:50%}
.cat{left:372px;top:75px;width:145px;height:50px;background:var(--navy);color:#fff;font-size:18px;display:flex;align-items:center;padding-left:12px}
.search{left:517px;top:75px;width:341px;height:50px;border:1px solid #ccc;font-size:11px;color:#555;padding:17px 0 0 25px}
.phone{left:910px;top:75px;display:flex;gap:12px;align-items:center}
.phone i{width:50px;height:50px;border-radius:50%;background:var(--navy);display:flex;align-items:center;justify-content:center}
.phone small{font-size:11px;display:block}
.phone b{font-family:"Oswald",sans-serif;font-size:21px;color:var(--navy)}
/* nav */
.nav{top:157px;height:48px;background:var(--navy);color:#fff;font-size:11.5px;font-weight:700}
.nav .item{position:absolute;top:0;height:48px;line-height:48px}
.nav .home{left:268px;width:64px;background:var(--blue);text-align:center;top:8px;height:32px;line-height:32px}
.nav .circ{position:absolute;top:12px;width:26px;height:26px;border:1.5px solid #fff;border-radius:50%}
/* hero */
.hero{top:205px;height:593px;background:#fff}
.hero h1{left:111px;top:130px;font-size:54px;line-height:60px;color:var(--navy)}
.hero p{left:111px;top:275px;width:410px;font-size:13px;line-height:30px;color:#333}
.btn{display:flex;align-items:center;justify-content:center;font-family:"Oswald",sans-serif;font-weight:500;text-transform:uppercase;font-size:16px}
.btn-dark{background:var(--navy);color:#fff}
.btn-line{border:2px solid var(--navy);color:var(--navy);background:#fff}
.btn-blue{background:var(--blue);color:#fff;box-shadow:0 3px 6px rgba(0,0,0,.25)}
.hero .btn{left:111px;top:395px;width:186px;height:53px}
.hero-img{left:530px;top:15px;width:670px;height:540px;background:radial-gradient(circle at 30% 45%,#2f6fd6 0 22%,transparent 23%),radial-gradient(circle at 55% 60%,#f2c418 0 14%,transparent 15%),radial-gradient(circle at 82% 45%,#8a8f95 0 25%,transparent 26%),#fff}
.arrow{width:42px;height:42px;border-radius:50%;background:var(--blue);display:flex;align-items:center;justify-content:center}
/* features */
.features{top:798px;height:190px;display:flex}
.feat{width:300px;height:190px;color:#fff;text-align:center;padding-top:30px;font-size:13.5px;line-height:26px}
.feat:nth-child(odd){background:var(--navy)}
.feat:nth-child(even){background:var(--blue)}
.feat h3{font-size:17px;margin-top:6px;line-height:24px}
/* welcome */
.welcome{top:988px;height:384px;background:var(--mist);text-align:center}
.welcome h2{margin-top:85px;font-size:37px;color:var(--navy)}
.welcome h2 span{color:var(--blue)}
.welcome h4{margin-top:20px;font-size:17px;color:#111}
.welcome p{width:780px;margin:25px auto 0;font-size:13.5px;line-height:30px;color:#333}
/* products */
.products{top:1372px;height:838px}
.title{font-size:37px;color:var(--navy)}
.title span{color:var(--blue);border-bottom:3px solid var(--navy)}
.card{position:absolute;width:474px;height:258px;background:#fff;box-shadow:0 0 10px rgba(0,0,0,.22)}
.card h3{position:absolute;left:20px;top:18px;font-size:17px;color:var(--navy)}
.card ul{position:absolute;left:20px;top:60px;list-style:none;font-size:12.5px;line-height:26px}
.card .btn{position:absolute;left:20px;top:178px;width:186px;height:53px}
.card .pic{position:absolute;right:20px;top:20px;width:225px;height:218px;border-radius:6px}
/* reviews */
.reviews{top:2210px;height:708px;background:linear-gradient(180deg,#1f72b8,#2d8fd0 60%,#1c6fb4)}
.reviews .title{color:#fff;left:108px;top:85px;position:absolute}
.badge{position:absolute;left:111px;width:152px;height:40px;color:#fff;font-family:"Roboto",sans-serif;font-weight:700;font-size:17px;display:flex;align-items:center;justify-content:center}
.rev{position:absolute;width:489px;height:161px;background:#fff;padding:18px 24px;font-size:13px;line-height:26px;color:#333;box-shadow:0 2px 8px rgba(0,0,0,.2)}
.rev h5{font-family:"Oswald",sans-serif;font-weight:500;font-size:14px;color:#222;margin-bottom:10px}
.stars{color:#f28c1c;letter-spacing:2px;margin-left:20px;font-size:14px}
.rev .src{position:absolute;left:24px;bottom:14px;font-size:11px;font-weight:700;color:var(--navy)}
.rev .recent{position:absolute;right:50px;bottom:10px;font-size:10.5px}
/* pricing */
.pricing{top:2918px;height:719px}
.plan{position:absolute;width:311px;height:363px;background:#fff;box-shadow:0 0 10px rgba(0,0,0,.22);text-align:center}
.plan .ph{height:53px;line-height:53px;font-size:19px;color:#fff}
.plan .price{font-family:"Oswald",sans-serif;font-size:34px;color:var(--blue);margin-top:8px}
.plan .vat{font-size:12.5px;font-weight:500;margin-top:-2px}
.plan p{font-size:12.5px;line-height:30px;margin-top:12px;padding:0 30px}
.pay{display:flex;justify-content:center;gap:16px;margin-top:12px;font-weight:700;font-size:17px;color:var(--navy)}
.plan .btn{width:170px;height:43px;margin:22px auto 0;font-size:15px}
/* newsletter */
.news{top:3637px;height:236px;background:var(--navy);color:#fff}
.news h2{position:absolute;left:103px;top:75px;font-size:35px}
.news p{position:absolute;left:100px;top:137px;font-size:12.5px}
.news .field{position:absolute;left:668px;top:93px;width:351px;height:52px;background:#fff;color:#555;font-size:12px;padding:19px 14px}
.news .go{position:absolute;left:1019px;top:93px;width:59px;height:52px;display:flex;align-items:center;justify-content:center}
/* footer */
.footer{top:3873px;height:314px}
.fcol{position:absolute;top:80px;font-size:13px;line-height:30px}
.fcol h4{font-size:17px;color:#111;margin-bottom:8px}
.fcol ul{list-style:none}
.fcol li:before{content:"»";margin-right:8px;color:#333}
.fcol .ci{display:flex;align-items:center;gap:8px;margin-bottom:15px}
.fsocial{display:flex;gap:35px;margin-top:10px}
.fsocial span{width:12px;height:12px;border-radius:50%;background:var(--navy)}
.copy{top:4187px;height:70px;background:var(--navy);color:#fff;font-size:12px}
.cards{position:absolute;left:846px;top:22px;display:flex;gap:14px}
.cards span{width:32px;height:22px;background:#dfe6ef;border-radius:2px}
</style>
</head>
<body>

<div class="section topbar">
  <div class="abs links">Newsletter &nbsp;| &nbsp;Contact Us &nbsp;| &nbsp;FAQs</div>
  <div class="abs social"><span></span><span></span><span></span><span></span><span></span></div>
  <div class="abs right">Covid-19 &nbsp;| &nbsp;Free Quote &nbsp;| &nbsp;English ▾</div>
</div>

<header class="section" style="top:50px;height:107px">
  <div class="abs brand" style="top:28px"><i></i>BORVELLO TRADE</div>
  <div class="abs cat head" style="top:25px">Categories ▾</div>
  <div class="abs search" style="top:25px">Search In All Categories
    <svg class="abs" style="right:14px;top:16px" width="16" height="16" viewBox="0 0 16 16"><circle cx="6.5" cy="6.5" r="5" fill="none" stroke="#333" stroke-width="2"/><path d="M10 10l5 5" stroke="#333" stroke-width="2"/></svg>
  </div>
  <div class="abs phone" style="top:25px">
    <i><svg width="20" height="20" viewBox="0 0 24 24"><path d="M6.6 10.8a15 15 0 006.6 6.6l2.2-2.2c.3-.3.7-.4 1-.2 1.1.4 2.3.6 3.6.6.6 0 1 .4 1 1V20c0 .6-.4 1-1 1A17 17 0 013 4c0-.6.4-1 1-1h3.5c.6 0 1 .4 1 1 0 1.3.2 2.5.6 3.6.1.3 0 .7-.2 1z" fill="#fff"/></svg></i>
    <div><small>Call Us Today</small><b>02/55018300</b></div>
  </div>
</header>

<nav class="section nav">
  <div class="item home">HOME</div>
  <div class="item" style="left:347px">PRODUCTS</div>
  <div class="item" style="left:445px">BLOG</div>
  <div class="item" style="left:508px">REVIEWS</div>
  <div class="item" style="left:597px">ELEMENTS</div>
  <div class="item" style="left:693px">CONTACT US</div>
  <div class="circ" style="left:832px"></div>
  <div class="circ" style="left:893px"></div>
</nav>

<section class="section hero">
  <div class="abs hero-img" role="img" aria-label="Blue, yellow and grey plastic canisters"></div>
  <h1 class="abs head">Tanichee Canestri<br>in Plastica</h1>
  <p class="abs">We are a young and dynamic company that combines twenty years of experience in the world of business services, with a deep and complete knowledge of the packaging .</p>
  <div class="abs btn btn-dark">Shop Now &nbsp;»</div>
  <div class="abs arrow" style="left:52px;top:272px"><svg width="12" height="12"><path d="M8 1L3 6l5 5" fill="none" stroke="#fff" stroke-width="2"/></svg></div>
  <div class="abs arrow" style="left:1105px;top:272px"><svg width="12" height="12"><path d="M4 1l5 5-5 5" fill="none" stroke="#fff" stroke-width="2"/></svg></div>
</section>

<section class="section features">
  <div class="feat">
    <svg width="60" height="60" viewBox="0 0 60 60" fill="none" stroke="#fff" stroke-width="2.5"><rect x="8" y="10" width="26" height="30"/><path d="M34 22h10l8 10v8H34z"/><circle cx="18" cy="46" r="5"/><circle cx="44" cy="46" r="5"/></svg>
    <h3 class="head">Fast Shipping</h3>Deliveries throughout Italy</div>
  <div class="feat">
    <svg width="60" height="60" viewBox="0 0 60 60" fill="none" stroke="#fff" stroke-width="2.5"><circle cx="28" cy="30" r="18"/><path d="M10 30h-2v10h4M46 30h2v10h-4"/><rect x="36" y="6" width="18" height="12"/></svg>
    <h3 class="head">Customer Service</h3>From 9:00 to 13:00<br>02/55018300</div>
  <div class="feat">
    <svg width="60" height="60" viewBox="0 0 60 60" fill="none" stroke="#fff" stroke-width="2.5"><rect x="12" y="6" width="30" height="44"/><path d="M18 16h18M18 24h18M18 32h10M34 50l18-18 4 4-18 18h-4z"/></svg>
    <h3 class="head">Certified Products</h3>Guaranteed, of quality and<br>in accordance with the law</div>
  <div class="feat">
    <svg width="60" height="60" viewBox="0 0 60 60" fill="none" stroke="#fff" stroke-width="2.5"><rect x="6" y="16" width="40" height="28"/><path d="M6 24h40M40 6l12 5v10c0 8-6 12-12 14-6-2-12-6-12-14V11z"/><path d="M35 20l4 4 7-8"/></svg>
    <h3 class="head">Secure Payments</h3>Paynest , Credit Cards,<br>Bank Transfer, Cash on Delivery</div>
</section>

<section class="section welcome">
  <h2 class="head"><span>Welcome to</span> Borvellotrade</h2>
  <h4 class="head">Borvellotrade online sale of supplies for bodies and companies</h4>
  <p>Plastic Containers, Metal Containers, Shelves, Lockers, Safety &amp; Environment, Pallets And Benches, Packaging Products, First Aid, Accident Prevention and PPE Delivery in 24 / 48H throughout Italy.Products at the best price, for the proper functioning of every institution and company.</p>
</section>

<section class="section products">
  <h2 class="abs head title" style="left:111px;top:85px"><span>Our</span> Products</h2>
  <svg class="abs" style="left:914px;top:93px" width="175" height="50" viewBox="0 0 175 50"><polygon points="0,0 80,0 95,50 0,50" fill="#2b8bcc"/><polygon points="80,0 175,0 175,50 95,50" fill="#13457c"/><path d="M48 17l-8 8 8 8M40 17l-8 8 8 8M124 17l8 8-8 8M132 17l8 8-8 8" stroke="#fff" stroke-width="2.5" fill="none"/></svg>

  <div class="card" style="left:111px;top:194px">
    <h3 class="head">Metal Containers</h3>
    <ul><li>Tinplate Cans</li><li>Buckets And Tipper Containers</li><li>Metal Drums</li><li>Tinplate Cans</li></ul>
    <div class="btn btn-dark">Shop Now &nbsp;»</div>
    <div class="pic" role="img" aria-label="Orange metal tipper container and tinplate cans" style="background:linear-gradient(135deg,#e2541f 55%,#b9bcbf 56%)"></div>
  </div>
  <div class="card" style="left:615px;top:194px">
    <h3 class="head">Plastic Containers</h3>
    <ul><li>Plastic Jars</li><li>Plastic Tipper Buckets</li><li>Plastic Drums And Drums</li><li>Plastic Bottles And Bottles</li></ul>
    <div class="btn btn-line">Shop Now &nbsp;»</div>
    <div class="pic" role="img" aria-label="Blue plastic water tanks and IBC container" style="background:linear-gradient(135deg,#1e7fd6 60%,#d9dde0 61%)"></div>
  </div>
  <div class="card" style="left:111px;top:485px">
    <h3 class="head" style="left:10px">Pallets and Pallets</h3>
    <ul><li>Plastic Pallet</li><li>Pressed Wood Pallet</li><li>Non-slip Modular Footboards</li><li>Pallet Cover</li></ul>
    <div class="btn btn-line">Shop Now &nbsp;»</div>
    <div class="pic" role="img" aria-label="Stacked pressed wood pallets" style="background:linear-gradient(135deg,#f3e7d6,#c49a66)"></div>
  </div>
  <div class="card" style="left:615px;top:485px">
    <h3 class="head">Emergency Room</h3>
    <ul><li>Boxes, Lockers And First Aid Kits</li><li>Adr Grants</li><li>Medication And Emergency Aids</li><li>Immobilization</li></ul>
    <div class="btn btn-line">Shop Now &nbsp;»</div>
    <div class="pic" role="img" aria-label="Open red first aid case" style="background:linear-gradient(135deg,#f1f1f1,#c8313a)"></div>
  </div>
</section>

<section class="section reviews" role="img" aria-label="Blurred blue warehouse background">
  <h2 class="head title">Our Client Reviews</h2>
  <div class="badge" style="top:200px;background:#fff;color:var(--navy);font-family:'Oswald',sans-serif;font-size:15px">ALL REVIEWS</div>
  <div class="badge" style="top:248px;background:#2e4c8a">Socialis</div>
  <div class="badge" style="top:298px;background:#1f1f1f">Trustora</div>
  <div class="badge" style="top:348px;background:#fff;color:#333">Searchly</div>

  <div class="rev" style="left:600px;top:94px">
    <h5>Lorem ipsum dolor sit amet, consectetur <span class="stars">★★★★★</span></h5>
    I bought a bin for water, the company is always available to solve any problem I would have preferred more care in the packaging.
    <span class="src">Socialis</span><span class="recent">Recent Review</span>
  </div>
  <div class="rev" style="left:515px;top:275px">
    <h5>Lorem ipsum dolor sit amet, consectetur <span class="stars">★★★★★</span></h5>
    <div style="margin-top:14px">The product meets expectations. Excellent value for money.</div>
    <span class="src">Searchly</span><span class="recent">Recent Review</span>
  </div>
  <div class="rev" style="left:360px;top:455px">
    <h5>Lorem ipsum dolor sit amet, consectetur <span class="stars">★★★★★</span></h5>
    UNRELIABLE company as (in my case = purchase of water tank in PE plastic of 5450 liters which had evident breakage defects after
    <span class="src">Trustora</span><span class="recent">Recent Review</span>
  </div>
</section>

<section class="section pricing">
  <h2 class="abs head title" style="left:0;width:1200px;text-align:center;top:75px"><span>Our</span> Pricing Plan</h2>
  <div class="plan" style="left:111px;top:229px">
    <div class="ph head" style="background:var(--blue)">Recommended</div>
    <div class="price">€ 2.15</div><div class="vat">VAT included (22%)</div>
    <p>sit amet, consectetur adipiscing elit, sed do eiusmod tempor incididunt ut labore et</p>
    <div class="pay"><span>Valora</span><span>Orbicard</span><span>Paynest</span></div>
    <div class="btn btn-blue">Shop Now</div>
  </div>
  <div class="plan" style="left:445px;top:177px">
    <div class="ph head" style="background:var(--navy)">Offers</div>
    <div class="price">€ 5.64</div><div class="vat">VAT included (22%)</div>
    <p>sit amet, consectetur adipiscing elit, sed do eiusmod tempor incididunt ut labore et</p>
    <div class="pay"><span>Valora</span><span>Orbicard</span><span>Paynest</span></div>
    <div class="btn btn-dark">Shop Now</div>
  </div>
  <div class="plan" style="left:778px;top:229px">
    <div class="ph head" style="background:var(--blue)">The + Sold</div>
    <div class="price">€ 1.80</div><div class="vat">VAT included (5%)</div>
    <p>sit amet, consectetur adipiscing elit, sed do eiusmod tempor incididunt ut labore et</p>
    <div class="pay"><span>Valora</span><span>Orbicard</span><span>Paynest</span></div>
    <div class="btn btn-blue">Shop Now</div>
  </div>
</section>

<section class="section news">
  <h2 class="head">Sign up for a newsletter</h2>
  <p>Sign up today to get 30% off your bill for your next purchase. Always get our latest offer</p>
  <div class="field">Enter The Email</div>
  <div class="go"><svg width="16" height="16" viewBox="0 0 16 16"><circle cx="6.5" cy="6.5" r="5" fill="none" stroke="#fff" stroke-width="2"/><path d="M10 10l5 5" stroke="#fff" stroke-width="2"/></svg></div>
</section>

<footer class="section footer">
  <div class="fcol" style="left:150px">
    <h4 class="head">Contact Us</h4>
    <div class="ci"><svg width="12" height="14" viewBox="0 0 12 16"><path d="M6 0a6 6 0 016 6c0 4-6 10-6 10S0 10 0 6a6 6 0 016-6z" fill="#13457c"/><circle cx="6" cy="6" r="2" fill="#fff"/></svg>Via Roma, 14 - 20090 Vedano</div>
    <div class="ci"><svg width="14" height="14"><rect width="14" height="14" rx="2" fill="#13457c"/></svg>2/55018300</div>
    <div class="ci"><svg width="16" height="12"><rect width="16" height="12" fill="#13457c"/><path d="M0 0l8 6 8-6" stroke="#fff" fill="none"/></svg>info@borvellotrade.it</div>
    <div class="fsocial"><span></span><span></span><span></span><span></span><span></span></div>
  </div>
  <div class="fcol" style="left:514px">
    <h4 class="head">Quick Links</h4>
    <ul><li>Home</li><li>About Us</li><li>Blogs</li><li>Products</li><li>Contact Us</li></ul>
  </div>
  <div class="fcol" style="left:696px">
    <h4 class="head">Customer Service</h4>
    <ul><li>Info Privacy</li><li>Terms and Conditions of Sale</li><li>Payments</li><li>Shipping and Withdrawals</li></ul>
  </div>
  <div class="fcol" style="left:943px">
    <h4 class="head">Services</h4>
    <ul><li>Online quote</li><li>FAQ</li><li>Guides and Tips</li><li>Catalogs</li><li>Regulations</li><li>Materials</li></ul>
  </div>
</footer>

<div class="section copy">
  <div class="abs" style="left:148px;top:28px">© Copyrights 2021 Company Name &nbsp;| &nbsp; All Rights Reserved</div>
  <div class="cards"><span></span><span></span><span></span><span></span><span></span></div>
</div>

</body>
</html>
```